Business cards design on a high standard

We advise clients on insurance and financial matters, since these clients pay for our advice, the design should have a high standard. Our logo should be included. From the colors we are open for everything.

Colors

Designer to choose colors to be used in the design.

```html
<!DOCTYPE html>
<html lang="en">
<head>
<meta charset="utf-8">
<title>Alpine Counsel – Business Cards</title>
<link rel="stylesheet" href="https://fonts.googleapis.com/css2?family=Montserrat:wght@700&family=Questrial&display=swap">
<style>
  :root {
    --page: #ececec;
    --card-white: #f4f4f4;
    --brand-red: #c91a21;
    --text-grey: #6d6e71;
    --rule-grey: #8a8b8d;
    --white: #ffffff;
  }
  * { box-sizing: border-box; margin: 0; padding: 0; }
  html, body {
    width: 1200px; height: 1200px; overflow: hidden;
    background: var(--page);
  }
  .sheet { position: relative; width: 1200px; height: 1200px; }
  .card {
    position: absolute; left: 227px; width: 745px; height: 425px;
  }
  .card--front { top: 135px; background: var(--card-white); }
  .card--back  { top: 638px; background: var(--brand-red); }

  .wordmark {
    position: absolute;
    font-family: "Montserrat", sans-serif; font-weight: 700;
    line-height: 1; text-transform: uppercase;
  }
  .wordmark__main { display: block; letter-spacing: 1px; }
  .wordmark__sub  { display: block; letter-spacing: 9px; }

  .card--front .wordmark { left: 40px; top: 178px; color: var(--brand-red); }
  .card--front .wordmark__main { font-size: 62px; }
  .card--front .wordmark__sub  { font-size: 30px; margin-top: 8px; padding-left: 4px; }

  .card--back .wordmark {
    left: 0; right: 0; top: 152px; text-align: center; color: var(--white);
  }
  .card--back .wordmark__main { font-size: 76px; }
  .card--back .wordmark__sub  { font-size: 37px; margin-top: 10px; letter-spacing: 12px; }

  .details {
    position: absolute; left: 467px; top: 0; right: 0; height: 100%;
    font-family: "Questrial", sans-serif; color: var(--text-grey);
  }
  .person__name {
    position: absolute; top: 77px;
    font-family: "Montserrat", sans-serif; font-weight: 700;
    font-size: 22px; color: var(--brand-red); letter-spacing: .3px;
  }
  .person__title { position: absolute; top: 106px; font-size: 17px; }
  .rule {
    position: absolute; top: 151px; left: 0; right: 0;
    height: 2px; background: var(--rule-grey);
  }
  .address { position: absolute; top: 182px; font-size: 17px; line-height: 24px; font-style: normal; }
  .contacts { position: absolute; top: 251px; list-style: none; font-size: 17px; }
  .contacts li { display: flex; align-items: center; height: 24px; }
  .contacts svg { width: 18px; height: 18px; margin-right: 10px; flex: none; }
  .contacts .accent { color: var(--brand-red); }
</style>
</head>
<body>
<main class="sheet">
  <section class="card card--front" aria-label="Card front">
    <div class="wordmark">
      <span class="wordmark__main">Alpine</span>
      <span class="wordmark__sub">Counsel</span>
    </div>
    <div class="details">
      <h1 class="person__name">MARTIN KELLER</h1>
      <p class="person__title">Managing Director</p>
      <div class="rule"></div>
      <address class="address">P.O. Box 4182 Cedar Falls<br>Montana 59410</address>
      <ul class="contacts">
        <li>
          <svg viewBox="0 0 18 18" aria-hidden="true"><circle cx="9" cy="9" r="9" fill="#c91a21"/><path d="M5 7.5c0-1.5 8-1.5 8 0v1h-2V7.8H7v.7H5z M6.5 9.5h5l1 3.5h-7z" fill="#fff"/></svg>
          <span>000 0000 00 00</span>
        </li>
        <li>
          <svg viewBox="0 0 18 18" aria-hidden="true"><circle cx="9" cy="9" r="9" fill="#c91a21"/><rect x="6" y="4" width="6" height="10" rx="1" fill="none" stroke="#fff" stroke-width="1.4"/></svg>
          <span>000 0000 00 00</span>
        </li>
        <li>
          <svg viewBox="0 0 18 18" aria-hidden="true"><circle cx="9" cy="9" r="9" fill="#c91a21"/><rect x="4.5" y="6" width="9" height="6.5" fill="none" stroke="#fff" stroke-width="1.2"/><path d="M4.5 6l4.5 3.5L13.5 6" fill="none" stroke="#fff" stroke-width="1.2"/></svg>
          <span>info@alpinecounsel.com</span>
        </li>
        <li>
          <svg viewBox="0 0 18 18" aria-hidden="true"><circle cx="9" cy="9" r="9" fill="#c91a21"/><circle cx="9" cy="9" r="5" fill="none" stroke="#fff" stroke-width="1.2"/><path d="M4 9h10M9 4c-2.5 3-2.5 7 0 10M9 4c2.5 3 2.5 7 0 10" fill="none" stroke="#fff" stroke-width="1"/></svg>
          <span>www.<span class="accent">alpinecounsel</span>.com</span>
        </li>
      </ul>
    </div>
  </section>

  <section class="card card--back" aria-label="Card back">
    <div class="wordmark">
      <span class="wordmark__main">Alpine</span>
      <span class="wordmark__sub">Counsel</span>
    </div>
  </section>
</main>
</body>
</html>
```